Recruitment Site Design

We need a design for the login page, about page, and inner pages of a recruitment site for an oil and gas company. Design should be modern, sleek, professional and colors can be blue, green, white, orange or any other recommended colors.

Please also take into consideration that once the users login, they will need to access a form to fill in their information.

** UPDATE: Kindly provide a design for the inner information page consistent with the outer design. Attached is a picture of the basic structure. ***
Updates

Please provide a design for inner pages as shown in the design brief consistent with the registration page provided. 

Reason: We're extending it to get more inside pages.

Target Market(s)

Professionals looking for a career in the oil and gas industry in the Middle East.

Industry/Entity Type

Oil And Gas

Requirements
Must have
• Sleek design

```html
<!DOCTYPE html>
<html lang="en">
<head>
<meta charset="utf-8">
<title>PetroRecruit – Oil &amp; Gas Careers</title>
<link href="https://fonts.googleapis.com/css2?family=Arimo:wght@400;700&display=swap" rel="stylesheet">
<style>
:root{
  --blue:#2a5db5;
  --blue-dark:#1c4696;
  --blue-light:#4d7fd0;
  --text:#333;
  --muted:#555;
  --line:#d6d6d6;
  --panel:#f1f1f1;
  --panel-head:#e4e4e4;
  --red:#e8141b;
  --page-top:#f4f4f4;
  --page-mid:#d9d9d9;
  --footer:#5a5a5a;
}
*{box-sizing:border-box;margin:0;padding:0}
html,body{width:1200px;height:944px;overflow:hidden}
body{font-family:"Arimo",Arial,sans-serif;color:var(--text);position:relative;
  background:linear-gradient(#fafafa 0,#e9e9e9 500px,#d4d4d4 848px,var(--footer) 848px,#3f3f3f 944px)}
.abs{position:absolute}
.rig-photo{left:0;top:252px;width:170px;height:596px;
  background:linear-gradient(#7f9dc4 0%,#b7c9de 35%,#8a97a3 55%,#2f5d93 75%,#1c3f6e 100%)}
.person-photo{left:1030px;top:60px;width:170px;height:788px;
  background:linear-gradient(90deg,#e9e9e9 0%,#d9d9d9 40%,#2b2b2b 60%,#1c1c1c 100%)}
.top-links{top:14px;left:820px;font-size:13px;color:#333;display:flex;gap:12px}
.sheet{left:164px;top:48px;width:877px;height:820px;background:#fff;border-radius:6px;
  box-shadow:0 0 14px rgba(0,0,0,.35)}
.brand{left:190px;top:80px;font-size:44px;color:var(--blue);letter-spacing:-1px}
.slogan{left:202px;top:130px;font-size:13px;color:#444}
.date{right:190px;top:146px;font-size:11px;color:#222}
.nav{left:172px;top:170px;width:857px;height:40px;border-radius:4px;
  background:linear-gradient(var(--blue-light),var(--blue) 50%,var(--blue-dark));display:flex;align-items:center}
.nav a{color:#fff;font-size:11.5px;text-decoration:none;padding:0 13px;line-height:40px;border-right:1px solid rgba(255,255,255,.35)}
.search{position:absolute;right:8px;top:7px;width:170px;height:26px;background:#fff;border-radius:4px;
  font-size:11px;font-style:italic;color:#444;padding:7px 9px}
.search svg{position:absolute;right:5px;top:3px}
.slider{left:176px;top:228px;width:582px;height:249px;border:3px solid #e6e6e6;
  box-shadow:0 6px 10px rgba(0,0,0,.25)}
.slider .photo{width:100%;height:100%;background:linear-gradient(#dfe8f0 0%,#b9c4cc 40%,#7d8891 75%,#555e66 100%)}
.arrow{top:100px;width:32px;height:38px;background:#fff;display:flex;align-items:center;justify-content:center}
.dots{left:432px;top:489px;display:flex;gap:3px}
.dots span{width:14px;height:14px;border-radius:50%;border:2px solid #888;background:#fff}
.dots span.on{background:var(--red)}
.cats{left:174px;top:516px;width:191px;height:186px;border:1px solid var(--line);border-radius:3px;background:#fff}
.cats li{list-style:none;font-size:11px;padding:0 0 0 22px;height:26.5px;line-height:26.5px;border-bottom:1px solid #e3e3e3;position:relative}
.cats li::before{content:"";position:absolute;left:10px;top:10px;border-left:5px solid #444;border-top:3px solid transparent;border-bottom:3px solid transparent}
.welcome{left:376px;top:516px;width:385px;height:186px;border:1px solid var(--line);border-radius:3px;padding:12px 14px}
.welcome h1{font-size:21px;font-weight:400;color:#222;margin-bottom:12px}
.welcome p{font-size:11.5px;line-height:15px;color:#333;text-indent:28px}
.benefits{left:174px;top:714px;width:587px;height:144px;border:1px solid var(--line);border-radius:3px;background:var(--panel)}
.phead{height:31px;background:linear-gradient(#f4f4f4,#dcdcdc);border-bottom:1px solid var(--line);
  font-size:14px;color:#333;padding:0 14px;line-height:31px;position:relative}
.phead .tog{position:absolute;right:12px;top:8px;width:17px;height:16px;background:#444;border-radius:2px}
.phead .tog::after{content:"";position:absolute;left:4px;top:6px;border-top:5px solid #fff;border-left:4.5px solid transparent;border-right:4.5px solid transparent}
.benefit-row{position:absolute;left:42px;top:50px;width:500px;height:72px;background:#fff;display:flex;padding:18px 10px 0;gap:14px;box-shadow:0 0 4px rgba(0,0,0,.2)}
.benefit-row div{font-size:11px;line-height:15px;padding-left:12px;position:relative;width:155px}
.benefit-row div::before{content:"";position:absolute;left:0;top:4px;width:8px;height:8px;border-radius:50%;background:var(--blue)}
.side{left:770px;width:259px;border:1px solid var(--line);border-radius:3px;background:var(--panel)}
.login{top:228px;height:120px}
.field{position:absolute;left:12px;width:142px;height:21px;background:#fff;border:1px solid #ccc}
.flabel{position:absolute;left:168px;font-size:11px}
.forgot{position:absolute;left:12px;top:95px;font-size:10.5px;text-decoration:underline}
.btn{position:absolute;background:var(--red);color:#fff;font-size:12px;font-weight:700;text-align:center;border-radius:2px}
.register{top:358px;height:35px}
.register .phead{height:33px;line-height:33px;border:0}
.jobs{top:400px;height:305px}
.jobs table{width:100%;border-collapse:collapse;font-size:10.5px}
.jobs td{height:36px;border-bottom:1px solid #dedede;padding:0 6px}
.jobs td:first-child{width:56px}
.jobs td:last-child{text-align:right;width:66px}
.viewall{position:absolute;right:12px;bottom:6px;font-size:11px;color:var(--red);text-decoration:underline}
.news{top:712px;height:146px}
.news p{font-size:10.5px;line-height:14px;padding:10px 12px 0 14px;color:#222}
.email{position:absolute;left:12px;top:84px;width:160px;height:26px;background:#fff;border:1px solid #ccc;font-size:11px;padding:7px 9px}
.agree{position:absolute;left:12px;top:122px;font-size:10.5px;display:flex;gap:7px;align-items:center}
.agree span{width:11px;height:11px;border:1px solid #aaa;background:#fff}
.footer-links{top:876px;left:0;width:1200px;display:flex;justify-content:center;font-size:11px;color:#fff}
.footer-links span{padding:0 11px;border-right:1px solid #ccc;line-height:12px}
.footer-links span:last-child{border:0}
.copyright{top:918px;left:0;width:1200px;text-align:center;font-size:10.5px;color:#fff}
</style>
</head>
<body>
<div class="abs rig-photo" role="img" aria-label="Offshore oil platform at sea under a blue sky"></div>
<div class="abs person-photo" role="img" aria-label="Business woman in a dark suit extending her hand"></div>

<nav class="abs top-links"><span>Login</span><span>|</span><span>Register</span><span>|</span><span>Contact Us</span></nav>

<div class="abs sheet"></div>
<div class="abs brand">PetroRecruit</div>
<div class="abs slogan">The slogan of your will be here</div>
<div class="abs date">Wednesday, 7th November, 2012</div>

<nav class="abs nav">
  <a>HOME</a><a>ABOUT US</a><a>SEARCH JOBS</a><a>CANDIDATES</a><a>RECRUITERS</a><a>FAQ'S</a><a>BLOGS</a><a>ADVICE</a>
  <div class="search">Search
    <svg width="22" height="20" viewBox="0 0 22 20"><circle cx="9" cy="8" r="6" fill="none" stroke="#2a5db5" stroke-width="2.5"/><line x1="13" y1="12" x2="19" y2="17" stroke="#2a5db5" stroke-width="3"/></svg>
  </div>
</nav>

<div class="abs slider">
  <div class="photo" role="img" aria-label="Oil refinery with steel towers and pipework"></div>
  <div class="abs arrow" style="left:0"><svg width="14" height="18"><path d="M11 2 3 9l8 7" fill="none" stroke="#333" stroke-width="3"/></svg></div>
  <div class="abs arrow" style="right:0"><svg width="14" height="18"><path d="M3 2l8 7-8 7" fill="none" stroke="#333" stroke-width="3"/></svg></div>
</div>
<div class="abs dots"><span class="on"></span><span></span><span></span><span></span></div>

<ul class="abs cats">
  <li>Oil Trading</li><li>Shipping &amp; Operations</li><li>Middle &amp; Back Office</li><li>Fuel Sales &amp; Distribution</li><li>Lubricants &amp; Chemicals</li><li>Oil Refining</li><li style="border:0">Gas &amp; Power</li>
</ul>

<section class="abs welcome">
  <h1>Welcome to this site.com</h1>
  <p>Lorem ipsum dolor sit amet, consecteteur adipiscing elit. set diem nonumy in convallis gravida neque. Nulla gravida vestibulum metis a acumsan, aliquam in sagitis ut. Solicitudin sed massa ud enim veniam. Curabitur tempus sem vitae mi vestibulum volutpat malesuada erat vestibulum. Sed aliquam dolor at dolor consequat gravida. Fusce mineque tempus nec fequat sit amet . Tincidunt ut leo. Nam semper ornare enim.</p>
</section>

<section class="abs benefits">
  <div class="phead">Benefits for Candidates</div>
  <div class="abs arrow" style="left:10px;top:62px;width:20px;height:36px;background:#ddd"><svg width="10" height="16"><path d="M8 2 2 8l6 6" fill="none" stroke="#333" stroke-width="2.5"/></svg></div>
  <div class="abs arrow" style="right:10px;top:62px;width:20px;height:36px;background:#ddd"><svg width="10" height="16"><path d="M2 2l6 6-6 6" fill="none" stroke="#333" stroke-width="2.5"/></svg></div>
  <div class="benefit-row">
    <div>Create a FREE virtual CV and let recruiters find you</div>
    <div>Create a FREE virtual CV and let recruiters find you</div>
    <div>Create a FREE virtual CV and let recruiters find you</div>
  </div>
</section>

<section class="abs side login">
  <div class="phead">MEMBERS AREA&nbsp; - Login<span class="tog"></span></div>
  <div class="field" style="top:43px"></div><span class="flabel" style="top:47px">Username</span>
  <div class="field" style="top:68px"></div><span class="flabel" style="top:72px">Password</span>
  <span class="forgot">Forgott Your Password?</span>
  <div class="btn" style="left:168px;top:90px;width:72px;height:20px;line-height:20px">LOG IN</div>
</section>

<section class="abs side register"><div class="phead">Not Member? Register Here<span class="tog"></span></div></section>

<section class="abs side jobs">
  <div class="phead">LATEST JOBS<span class="tog"></span></div>
  <table>
    <tr><td>Vietnam</td><td>offshore structural engineer</td><td>negotiable</td></tr>
    <tr><td>UK</td><td>Safety Coach</td><td>US$95000</td></tr>
    <tr><td>UK</td><td>Senior Process engineer</td><td></td></tr>
    <tr><td>Gabon</td><td>NDT Inspector</td><td>negotiable</td></tr>
    <tr><td>UK</td><td>Estimator O&amp;G</td><td>Excellent</td></tr>
    <tr><td>UK</td><td>Civil Underground engineer</td><td>negotiable</td></tr>
    <tr><td style="border:0">UK</td><td style="border:0">Safety Coach</td><td style="border:0">US$95000</td></tr>
  </table>
  <span class="viewall">View All</span>
</section>

<section class="abs side news">
  <div class="phead">NEWSLETTER<span class="tog"></span></div>
  <p>If you want receive a news about jobs updtae from this site daily, please enter your email address.</p>
  <div class="email">Your email address</div>
  <div class="btn" style="left:178px;top:84px;width:70px;height:26px;line-height:26px;font-size:13px">SUBMIT</div>
  <div class="agree"><span></span>by clicking this button, you agree with our terms</div>
</section>

<nav class="abs footer-links">
  <span>Home</span><span>About Us</span><span>Search Jobs</span><span>Candidates</span><span>Recruiters</span><span>FAQ'S</span><span>Blogs</span><span>Log in</span><span>Register</span><span>Terms of Use</span><span>Privacy Policy</span><span>Contact Us</span>
</nav>
<div class="abs copyright">Copyright © 2012, petrorecruit-careers.com. All rights reserved.</div>
</body>
</html>
```